Business card and insta posting square

This is for 2 separate projects...

1...a double sided business card for online business (no address) to hand to businesses to get them to list their details on my online directory. the butterfly logo is to be used on the business card.

2.... a posting square for Instagram to write inspirational quotes over the top of to post....with a small butterfly logo somewhere on it (in a corner maybe)....the square is to have a thin, solid green outline around the edge of it, and a faded picture through the background that will allow me to write text over the top of it that will be easily readable.
I would like the same box for all Instagram quote posts for consistency ..

Target Market(s)

spiritual , yoga, meditation, wellness......

Industry/Entity Type

Wellness

Contact Information for Business Card

Details for Business Card...
Wandering The Quiet Tide
Your Complete Wellness Directory
www.wanderingthequiettide.example
insta/FB/pinterest/twitter
*List Your Business for FREE *

Colors
33b8a4
34a7d8
3276b5
876aae
9bcb3c

Requirements
Must have
• butterfly logo included on business card
• insta post square can use the butterfly logo OR the WTQT green square uploaded in the images
Nice to have
• greens

```html
<!DOCTYPE html>
<html lang="en">
<head>
<meta charset="utf-8">
<title>Wandering The Quiet Tide — Business Card</title>
<link rel="stylesheet" href="https://fonts.googleapis.com/css2?family=Kalam:wght@400;700&family=Allura&family=Libre+Baskerville:wght@700&display=swap">
<style>
  :root {
    --teal: #33b8a4;
    --sky: #34a7d8;
    --blue: #3276b5;
    --violet: #876aae;
    --purple: #5a2d8c;
    --green: #9bcb3c;
    --leaf: #2f9a45;
    --lavender: #e6e1ee;
    --ghost: #d6cfe2;
    --paper: #ffffff;
    --backdrop: #ebe7e1;
  }
  * { margin: 0; padding: 0; box-sizing: border-box; }
  html, body {
    width: 900px; height: 1200px; overflow: hidden;
    background: var(--backdrop);
  }
  .card {
    position: absolute; left: 80px; width: 733px; height: 428px;
    background: var(--paper); border-radius: 22px; overflow: hidden;
    box-shadow: 0 4px 14px rgba(0,0,0,0.18);
  }
  .card--front { top: 128px; }
  .card--back { top: 646px; }

  .headline {
    position: absolute; left: 38px; top: 48px;
    font-family: "Kalam", cursive; font-weight: 400; font-size: 41px; line-height: 56px;
    background: linear-gradient(90deg, var(--purple) 0%, var(--blue) 45%, var(--teal) 80%, var(--green) 100%);
    -webkit-background-clip: text; background-clip: text; color: transparent;
  }
  .website {
    position: absolute; left: 40px; top: 222px;
    font-family: "Libre Baskerville", serif; font-weight: 700; font-size: 15px;
    color: var(--purple);
  }
  .social-row { position: absolute; left: 38px; top: 254px; display: flex; gap: 6px; }
  .social-dot {
    width: 30px; height: 30px; border-radius: 50%;
    background: linear-gradient(135deg, var(--green), var(--teal) 45%, var(--violet));
  }
  .offer {
    position: absolute; left: 38px; top: 350px;
    font-family: "Kalam", cursive; font-weight: 400; font-size: 24px; color: var(--purple);
  }
  .swarm { position: absolute; border-radius: 40% 60% 55% 45%; }
  .swarm--front {
    left: 398px; top: 8px; width: 92px; height: 240px;
    background: linear-gradient(160deg, rgba(155,203,60,0.55), rgba(51,184,164,0.5) 60%, rgba(52,167,216,0.45));
  }
  .brand-mark {
    position: absolute; left: 500px; top: 70px; width: 233px;
    display: flex; flex-direction: column; align-items: center; gap: 16px;
  }
  .brand-dot { width: 120px; height: 120px; border-radius: 50%; background: var(--violet); }
  .brand-name {
    font-family: "Kalam", cursive; font-weight: 400; font-size: 26px; line-height: 32px;
    color: var(--purple); text-align: center;
  }

  .back-title {
    position: absolute; left: 0; width: 733px; top: 162px; text-align: center;
    font-family: "Allura", cursive; font-weight: 400; font-size: 40px; line-height: 50px;
    color: var(--leaf);
  }
  .back-tagline {
    position: absolute; left: 0; width: 733px; top: 225px; text-align: center;
    font-family: "Kalam", cursive; font-weight: 400; font-size: 21px; color: var(--sky);
  }
  .swarm--back-faint {
    left: 420px; top: 0; width: 313px; height: 428px;
    background: linear-gradient(200deg, rgba(230,225,238,0.95), rgba(230,225,238,0.55));
    border-radius: 55% 0 0 45%;
  }
  .brand-name--faint {
    position: absolute; left: 535px; top: 300px; width: 190px;
    font-family: "Kalam", cursive; font-weight: 400; font-size: 24px; line-height: 30px;
    color: var(--ghost); text-align: center;
  }
  .swarm--back-corner {
    left: 0; top: 255px; width: 130px; height: 173px;
    border-radius: 0 60% 0 0;
    background: linear-gradient(30deg, rgba(51,184,164,0.55), rgba(155,203,60,0.45));
  }
</style>
</head>
<body>
  <section class="card card--front">
    <h1 class="headline">Your Complete<br>Wellness Directory</h1>
    <p class="website">www.wanderingthequiettide.example</p>
    <div class="social-row">
      <span class="social-dot"></span><span class="social-dot"></span>
      <span class="social-dot"></span><span class="social-dot"></span>
    </div>
    <p class="offer">List Your Business for FREE</p>
    <div class="swarm swarm--front" role="img" aria-label="Small green and teal butterflies fluttering upward"></div>
    <div class="brand-mark">
      <span class="brand-dot"></span>
      <span class="brand-name">Wandering The<br>Quiet Tide</span>
    </div>
  </section>

  <section class="card card--back">
    <div class="swarm swarm--back-faint" role="img" aria-label="Faint lavender butterflies drifting across the right side"></div>
    <span class="brand-name--faint">Wandering The<br>Quiet Tide</span>
    <div class="swarm swarm--back-corner" role="img" aria-label="Small green and teal butterflies in the lower left corner"></div>
    <h2 class="back-title">Wandering The Quiet Tide</h2>
    <p class="back-tagline">Your Complete Wellness Directory</p>
  </section>
</body>
</html>
```